Bright Lantern Path (BRLP) Business Card - company with a mission

Note* The file attached... orange with "Bright Lantern PATH" (in CAPS) is our logo. I am also open to having the text "bright lantern path" OUTSIDE the orange round logo for business card (so yes, you may take the text out).

The info: (the following info are separate. So either you can use Martin or Beatrice for now, but that will be 2 separate cards, not together in one card. Thanks!!

Martin K Doyle
202.555.0147
martin@brightlanternpath.example
Managing Partner

Beatrice M Orr
202.555.0183
beatrice@brightlanternpath.example
Managing Partner

Our website: www.brightlanternpath.example

BRLP LLC stands for Bright Lantern Path (non profit arm is called lantern path foundation)—our business is based out of New York City and has a non-profit arm where for every bar of soap you purchase, we donate a bar (don’t want any designs that limits us to only soap). Currently working with South Africa. We want the focus to be organic/natural soap with a mission.

Looking for a clean, fresh design.

Industry/Entity Type

Non-Profit

Requirements
Must have
• Clean, fresh, refreshing. Design should not be too busy.

```html
<!DOCTYPE html>
<html lang="en">
<head>
<meta charset="utf-8">
<title>Bright Lantern Path – Business Card</title>
<link href="https://fonts.googleapis.com/css2?family=Questrial&display=swap" rel="stylesheet">
<style>
  :root {
    --canvas-bg: #ece9e4;
    --card-dark: #333335;
    --card-light: #ffffff;
    --brand-orange: #f2ad6c;
    --text-light: #f4f4f4;
    --shadow: rgba(0, 0, 0, 0.22);
  }
  * { box-sizing: border-box; margin: 0; padding: 0; }
  html, body {
    width: 1200px;
    height: 1000px;
    overflow: hidden;
  }
  body {
    background: var(--canvas-bg);
    font-family: "Questrial", "Century Gothic", sans-serif;
    position: relative;
  }
  .card {
    position: absolute;
    left: 220px;
    width: 760px;
    height: 434px;
    border-radius: 18px;
    overflow: hidden;
    box-shadow: 0 10px 26px var(--shadow);
  }
  .card-front {
    top: 46px;
    background: var(--card-dark);
    display: flex;
    align-items: center;
    justify-content: center;
  }
  .card-back {
    top: 520px;
    display: flex;
  }
  .brand-mark {
    display: flex;
    align-items: center;
    gap: 22px;
  }
  .brand-dot {
    width: 64px;
    height: 64px;
    border-radius: 50%;
    background: var(--brand-orange);
    flex: none;
  }
  .brand-name {
    color: var(--brand-orange);
    font-size: 44px;
    letter-spacing: 1px;
    line-height: 1;
  }
  .card-front .brand-name { font-size: 50px; }
  .card-back .brand-mark { gap: 16px; }
  .card-back .brand-dot { width: 46px; height: 46px; }
  .card-back .brand-name { font-size: 32px; }
  .back-brand {
    width: 50%;
    background: var(--card-light);
    display: flex;
    align-items: center;
    justify-content: center;
  }
  .back-details {
    width: 50%;
    background: var(--card-dark);
    color: var(--text-light);
    padding: 56px 0 0 0;
    text-align: center;
  }
  .person-name {
    color: var(--brand-orange);
    font-size: 27px;
    letter-spacing: 2px;
    text-transform: uppercase;
  }
  .person-title {
    font-size: 21px;
    margin-top: 6px;
  }
  .contact-list {
    list-style: none;
    margin-top: 78px;
    font-size: 19px;
    line-height: 34px;
  }
  .contact-label { color: var(--brand-orange); }
  .website {
    margin-top: 52px;
    font-size: 19px;
  }
  .website .highlight { color: var(--brand-orange); }
</style>
</head>
<body>
  <section class="card card-front" aria-label="Card front">
    <div class="brand-mark">
      <span class="brand-dot"></span>
      <span class="brand-name">Bright Lantern Path</span>
    </div>
  </section>

  <section class="card card-back" aria-label="Card back">
    <div class="back-brand">
      <div class="brand-mark">
        <span class="brand-dot"></span>
        <span class="brand-name">Bright Lantern Path</span>
      </div>
    </div>
    <div class="back-details">
      <h1 class="person-name">Martin K Doyle</h1>
      <p class="person-title">Managing Director</p>
      <ul class="contact-list">
        <li><span class="contact-label">P:</span> 202.555.0147</li>
        <li><span class="contact-label">E:</span> martin@brightlanternpath.example</li>
      </ul>
      <p class="website">www.<span class="highlight">brightlanternpath</span>.example</p>
    </div>
  </section>
</body>
</html>
```